Store Signage for New Location

I need a banner for my new location. It needs to communicate 1: our name, 2: our phone number 3: our message. This is going to be a 7 foot wide banner that is 4 feet tall. It needs to be a very high resolution design so it prints properly.

Our phone number is (555) 418-2097

Our Message: The HONEST alternative to the dealer.

Or: Your Honest Auto Service Center

"Honest" is our key word here.
Updates

Target Market(s)

Drive-by traffic.

Industry/Entity Type

Auto Repair

Requirements
Must have
• The name of our business: Fair Lane Auto Repair
• Our phone number: (555) 418-2097
• Our message: The HONEST alternative to the dealership.
• or: Your Honest Service Center
Nice to have
• I really just need a clean layout using the uploaded logo and font. It needs to be highly visible as a sign that is seen by drive-by traffic.
• I'd like the color scheme to be the same as what I have, however, you're more than welcome to add detail and color as needed.

```html
<!DOCTYPE html>
<html lang="en">
<head>
<meta charset="utf-8">
<title>Fair Lane Auto Repair – Banner</title>
<link rel="stylesheet" href="https://fonts.googleapis.com/css2?family=Open+Sans:ital,wght@0,800;1,800&family=Rajdhani:wght@600&display=swap">
<style>
  :root {
    --ink: #000000;
    --paper: #ffffff;
    --accent: #1fb8e6;
    --page: #e9ecef;
  }
  * { margin: 0; padding: 0; box-sizing: border-box; }
  html, body {
    width: 1200px;
    height: 825px;
    overflow: hidden;
    background: var(--page);
  }
  .banner {
    position: relative;
    width: 1200px;
    height: 825px;
    background: var(--paper);
    overflow: hidden;
  }
  .banner__top-stripe {
    position: absolute;
    left: 0; top: 0;
    width: 100%;
    height: 46px;
    background: var(--ink);
  }
  .brand {
    position: absolute;
    left: 0; top: 46px;
    width: 100%;
    height: 380px;
    display: flex;
    align-items: center;
    justify-content: center;
    gap: 60px;
  }
  .brand__mark {
    width: 190px;
    height: 190px;
    border-radius: 50%;
    background: var(--ink);
    flex: none;
  }
  .brand__name {
    font-family: "Open Sans", Arial, sans-serif;
    font-weight: 800;
    font-size: 96px;
    line-height: 1.08;
    color: var(--ink);
    text-align: center;
  }
  .message-band {
    position: absolute;
    left: 0; top: 426px;
    width: 100%;
    height: 399px;
    background: var(--ink);
    display: flex;
    flex-direction: column;
    align-items: center;
    justify-content: center;
    gap: 18px;
    padding: 0 40px;
  }
  .tagline {
    font-family: "Open Sans", Arial, sans-serif;
    font-weight: 800;
    font-size: 50px;
    line-height: 1.2;
    color: var(--paper);
    letter-spacing: 0.5px;
    white-space: nowrap;
  }
  .tagline__key {
    color: var(--accent);
    font-style: italic;
  }
  .phone {
    font-family: "Rajdhani", "Arial Narrow", sans-serif;
    font-weight: 600;
    font-size: 158px;
    line-height: 1;
    color: var(--accent);
    letter-spacing: 2px;
    white-space: nowrap;
  }
</style>
</head>
<body>
  <main class="banner">
    <div class="banner__top-stripe"></div>

    <header class="brand">
      <span class="brand__mark" aria-hidden="true"></span>
      <h1 class="brand__name">Fair Lane<br>Auto Repair</h1>
    </header>

    <section class="message-band">
      <p class="tagline">The <span class="tagline__key">HONEST</span> alternative to the dealer.</p>
      <p class="phone">(555) 418-2097</p>
    </section>
  </main>
</body>
</html>
```